Business Card Design Project

We are an incubator company that helps young entrepreneur to launch new ideas into the market. We will be targeting investors or likewise; Angels, young entrepreneurs and technopreneurs.

Our logo is being tasked by artswarm to design, therefore there is no logo for now.
You can us Lanternfield Pte Ltd as the logo for the time being.

Please let us have some versions of modern and yet professional designs; for words, you can indicate e.g (address), (Title)

thanks

Target Market(s)

young entrepreneurs
angels, investors

Industry/Entity Type

Business

Colors
3176b5
ffffff

Requirements
Must have
• able to project out our name; Lanternfield
Should not have
• Nothing childish or cartoon

```html
<!DOCTYPE html>
<html lang="en">
<head>
<meta charset="utf-8">
<title>Lanternfield Business Card</title>
<link rel="stylesheet" href="https://fonts.googleapis.com/css2?family=Lato:wght@400;700&display=swap">
<style>
  :root {
    --stage: #d7d4d3;
    --brand-blue: #3176b5;
    --brand-blue-bright: #1f6fd1;
    --band-text: #0d2f55;
    --card-white: #ffffff;
    --card-black: #141618;
    --card-black-soft: #24272b;
    --text-light: #f2f2f2;
    --divider: #5a5d61;
  }
  * { box-sizing: border-box; margin: 0; padding: 0; }
  html, body { width: 1200px; height: 900px; overflow: hidden; }
  body {
    background: var(--stage);
    font-family: "Lato", sans-serif;
    position: relative;
  }
  .card {
    position: absolute;
    top: 290px;
    width: 540px;
    height: 320px;
    border-radius: 26px;
    overflow: hidden;
  }
  .card-front { left: 30px; background: var(--card-white); }
  .card-back {
    left: 630px;
    background: radial-gradient(ellipse at 45% 40%, var(--card-black-soft), var(--card-black) 75%);
  }

  /* front: brand area */
  .brand-block {
    position: absolute;
    top: 0; left: 0; right: 0;
    height: 170px;
    display: flex;
    flex-direction: column;
    align-items: center;
    justify-content: center;
    gap: 14px;
  }
  .brand-square {
    width: 58px; height: 58px;
    background: var(--brand-blue);
    border-radius: 6px;
  }
  .brand-name {
    font-weight: 700;
    font-size: 30px;
    color: var(--brand-blue);
    letter-spacing: 1px;
  }
  .tagline-band {
    position: absolute;
    top: 170px; left: 0; right: 0;
    height: 14px;
    background: var(--brand-blue);
    display: flex;
    align-items: center;
    justify-content: center;
    font-size: 9px;
    letter-spacing: 10px;
    text-transform: uppercase;
    color: var(--band-text);
    font-weight: 700;
    white-space: nowrap;
  }
  .contact-panel {
    position: absolute;
    top: 184px; left: 0; right: 0; bottom: 0;
    background: var(--card-black);
    display: flex;
    padding: 18px 0 0 0;
  }
  .person {
    width: 200px;
    text-align: right;
    padding-right: 16px;
    border-right: 1px solid var(--divider);
    height: 92px;
  }
  .person-name { color: var(--brand-blue-bright); font-size: 18px; }
  .person-title { color: var(--text-light); font-size: 12px; margin-top: 4px; }
  .contact-list { list-style: none; padding-left: 14px; }
  .contact-list li {
    display: flex; align-items: center; gap: 8px;
    color: var(--text-light);
    font-size: 18px;
    line-height: 25px;
    white-space: nowrap;
  }
  .contact-list svg { width: 18px; height: 18px; fill: var(--brand-blue-bright); flex: none; }

  /* back */
  .back-brand {
    position: absolute; inset: 0;
    display: flex; flex-direction: column; align-items: center; justify-content: center;
    gap: 18px;
  }
  .back-brand .brand-square { width: 96px; height: 96px; border-radius: 10px; }
  .back-brand .brand-name { font-size: 48px; }
  .back-tagline {
    margin-top: -14px;
    font-size: 12px;
    letter-spacing: 3px;
    color: var(--brand-blue);
    text-transform: uppercase;
    font-weight: 700;
    white-space: nowrap;
  }
</style>
</head>
<body>
  <section class="card card-front">
    <div class="brand-block">
      <div class="brand-square"></div>
      <div class="brand-name">Lanternfield</div>
    </div>
    <div class="tagline-band">Launching Bold Ideas Onward</div>
    <div class="contact-panel">
      <div class="person">
        <div class="person-name">Dana Whitfield</div>
        <div class="person-title">Manager</div>
      </div>
      <ul class="contact-list">
        <li><svg viewBox="0 0 24 24"><path d="M6.6 10.8a15 15 0 0 0 6.6 6.6l2.2-2.2a1 1 0 0 1 1-.25 11.4 11.4 0 0 0 3.6.57 1 1 0 0 1 1 1V20a1 1 0 0 1-1 1A17 17 0 0 1 3 4a1 1 0 0 1 1-1h3.5a1 1 0 0 1 1 1c0 1.25.2 2.45.57 3.57a1 1 0 0 1-.25 1z"/></svg>555 014 2273</li>
        <li><svg viewBox="0 0 24 24"><path d="M12 2a10 10 0 1 0 0 20 10 10 0 0 0 0-20zm6.9 6h-2.9a15.6 15.6 0 0 0-1.4-3.6A8 8 0 0 1 18.9 8zM12 4c.8 1.2 1.5 2.5 1.9 4h-3.8c.4-1.5 1.1-2.8 1.9-4zM4.3 14a8 8 0 0 1 0-4h3.4a16 16 0 0 0 0 4zm.8 2h2.9c.3 1.3.8 2.5 1.4 3.6A8 8 0 0 1 5.1 16zM8 8H5.1a8 8 0 0 1 4.3-3.6C8.8 5.5 8.3 6.7 8 8zm4 12c-.8-1.2-1.5-2.5-1.9-4h3.8c-.4 1.5-1.1 2.8-1.9 4zm2.3-6H9.7a14.7 14.7 0 0 1 0-4h4.6a14.7 14.7 0 0 1 0 4zm.3 5.6c.6-1.1 1.1-2.3 1.4-3.6h2.9a8 8 0 0 1-4.3 3.6zm1.7-5.6a16 16 0 0 0 0-4h3.4a8 8 0 0 1 0 4z"/></svg>www.lanternfield.com</li>
        <li><svg viewBox="0 0 24 24"><path d="M3 5h18a1 1 0 0 1 1 1v12a1 1 0 0 1-1 1H3a1 1 0 0 1-1-1V6a1 1 0 0 1 1-1zm9 7.5L4 7.3V8l8 5.2L20 8v-.7z"/></svg>mara@lanternfield.com</li>
        <li><svg viewBox="0 0 24 24"><path d="M12 3l10 9h-3v9h-5v-6h-4v6H5v-9H2z"/></svg>Brookhaven, North Carolina</li>
      </ul>
    </div>
  </section>

  <section class="card card-back">
    <div class="back-brand">
      <div class="brand-square"></div>
      <div class="brand-name">Lanternfield</div>
      <div class="back-tagline">Launching Bold Ideas Onward</div>
    </div>
  </section>
</body>
</html>
```